依頼詳細
タイトル+20~30行のテキストが主。
テキストをお読みいただき雰囲気に合ったデザインをお願いします。
イメージ
重厚感、誠実、まじめ。
もし動画にするならBGMはカゼノワの「白い石の坂道」のイメージ。
曇り空に一筋の光
とか
全面的に黒い雰囲気の中に一滴の赤

或いは画像の中の青空を活かしても面白いかもしれません。
記載項目
・添付のテキスト
・背景に使う写真は添付ファイルを使ってもいいし、使わなくても構いません
・最後の「松浦産業株式会社」は検索ウィンドウとし、右側に「検索」ボタンをつけてください。
・チラシ最下段に「説明会情報は弊社HPでご確認ください」
サイズ
A4
ページ数
片面
希望イメージ
シンプル 複雑
単色 カラフル
暗い 明るい
日常 高級
遊び心 厳粛
未来的 伝統的
女性的 男性的
希望する色
水色系、グレー系
納品ファイル
• フォトショップ形式 (.psd)
補足説明
追加でお願いするポスターは約72cm×22cmで一般的なサイズ
合同企業説明会のときにブースを通る学生さんの足を止めるためのインパクト大なポスターを希望します。

希望通りのイメージで仕上げて頂きました。
ありがとうございます。

多数のご提案頂きありがとうございました。

```html
<!DOCTYPE html>
<html lang="ja">
<head>
<meta charset="utf-8">
<title>松浦産業株式会社 採用ポスター</title>
<link rel="stylesheet" href="https://fonts.googleapis.com/css2?family=Noto+Sans+JP:wght@400;500;700;900&display=swap">
<style>
  :root {
    --sky-top: #2d78cc;
    --sky-mid: #5ea4e2;
    --sky-low: #a8d2f1;
    --sky-base: #d8ecf8;
    --text-white: #ffffff;
    --ink-navy: #1c2f5a;
    --rock-light: #b9b6b0;
    --rock-dark: #5f5d59;
    --town-roof: #6d7480;
    --town-wall: #e4e6e8;
    --search-border: #1c2f5a;
    --search-fill: #ffffff;
  }
  * { margin: 0; padding: 0; box-sizing: border-box; }
  html, body { width: 846px; height: 1200px; overflow: hidden; }
  body { font-family: "Noto Sans JP", sans-serif; }
  .poster {
    position: relative;
    width: 846px;
    height: 1200px;
    overflow: hidden;
    background: linear-gradient(180deg, var(--sky-top) 0%, var(--sky-mid) 40%, var(--sky-low) 78%, var(--sky-base) 100%);
    color: var(--text-white);
  }
  .headline {
    position: absolute;
    left: 84px;
    top: 40px;
    font-size: 34px;
    font-weight: 900;
    line-height: 1.32;
    letter-spacing: 0.04em;
  }
  .headline span { display: block; }
  .headline .indent { padding-left: 42px; }
  .rock {
    position: absolute;
    left: 300px;
    top: 192px;
    width: 262px;
    height: 222px;
  }
  .message {
    position: absolute;
    left: 392px;
    top: 330px;
    width: 440px;
    font-weight: 500;
    letter-spacing: 0.03em;
  }
  .message .lead { font-size: 21px; line-height: 28px; font-weight: 700; margin-bottom: 66px; }
  .message .body { font-size: 13px; line-height: 24px; margin-bottom: 24px; }
  .message .body:last-child { margin-bottom: 0; }
  .message p span { display: block; white-space: nowrap; }
  .town {
    position: absolute;
    left: 0;
    bottom: 0;
    width: 846px;
    height: 150px;
  }
  .company {
    position: absolute;
    left: 0;
    top: 1070px;
    width: 846px;
    color: var(--ink-navy);
    text-align: center;
  }
  .company .tagline { font-size: 12px; font-weight: 700; letter-spacing: 0.06em; }
  .search {
    display: inline-flex;
    align-items: stretch;
    margin-top: 6px;
    border: 2px solid var(--search-border);
    background: var(--search-fill);
  }
  .search .name {
    font-size: 21px;
    font-weight: 900;
    letter-spacing: 0.05em;
    padding: 2px 18px;
    min-width: 260px;
    text-align: left;
  }
  .search .button {
    font-size: 15px;
    font-weight: 700;
    background: var(--search-border);
    color: var(--text-white);
    padding: 0 16px;
    display: flex;
    align-items: center;
  }
  .company .footer {
    margin-top: 10px;
    font-size: 13px;
    font-weight: 700;
    color: var(--text-white);
    letter-spacing: 0.05em;
  }
</style>
</head>
<body>
<main class="poster">
  <h1 class="headline">
    <span>スーツを着た仕事が</span>
    <span class="indent">幸せだと</span>
    <span class="indent">思い込んでないか？</span>
  </h1>

  <svg class="rock" viewBox="0 0 262 222" role="img" aria-label="宙に浮かぶ大きな灰色の岩の写真">
    <defs>
      <linearGradient id="rockTone" x1="0" y1="0" x2="1" y2="1">
        <stop offset="0" stop-color="var(--rock-light)"/>
        <stop offset="1" stop-color="var(--rock-dark)"/>
      </linearGradient>
    </defs>
    <polygon points="70,20 150,0 230,30 262,110 220,200 120,222 30,190 0,100" fill="url(#rockTone)"/>
  </svg>

  <section class="message">
    <p class="lead">
      <span>人生にゴールなんて無い。</span>
      <span>あるのは自分と世界との関わりだけだ。</span>
      <span>幸せを肯定するのは世界じゃない。</span>
      <span>自分自身だ。</span>
      <span>全ての価値観を捨てたとき、</span>
      <span>未来に何を掴むんだろう。</span>
    </p>
    <p class="body">
      <span>やりたいことが見つからないなんて当たり前だ。</span>
      <span>試しに周りの大人に聞いてみたらいい。</span>
      <span>「やりたいこと、仕事にできてますか？」</span>
      <span>きっと曖昧な答えしか返ってこない。</span>
    </p>
    <p class="body">
      <span>もう迷わない。</span>
      <span>面接じゃない。</span>
      <span>何者にもなれはしない。</span>
      <span>確かな答えは無い。</span>
      <span>自分探しなんてもう十分だ。</span>
    </p>
    <p class="body">
      <span>諦めよう。</span>
      <span>全てそこから始まる。</span>
    </p>
    <p class="body">
      <span>誰もがみな目的地なんてわかってない。</span>
      <span>それでも、</span>
      <span>それでも歩むしかない。</span>
    </p>
    <p class="body">
      <span>変わり続ける自分自身に何を期待するのだろう。</span>
    </p>
  </section>

  <svg class="town" viewBox="0 0 846 150" preserveAspectRatio="none" role="img" aria-label="空の下に並ぶ住宅街の屋根の写真">
    <defs>
      <linearGradient id="townTone" x1="0" y1="0" x2="0" y2="1">
        <stop offset="0" stop-color="var(--town-wall)" stop-opacity="0"/>
        <stop offset="0.35" stop-color="var(--town-wall)"/>
        <stop offset="1" stop-color="var(--town-roof)"/>
      </linearGradient>
    </defs>
    <rect width="846" height="150" fill="url(#townTone)"/>
  </svg>

  <div class="company">
    <p class="tagline">企業価値のその先を見据える</p>
    <div class="search">
      <span class="name">松浦産業株式会社</span>
      <span class="button">検索</span>
    </div>
    <p class="footer">説明会情報は弊社HPでご確認ください</p>
  </div>
</main>
</body>
</html>
```